Heron Yards LLC - Door Hanger for Residential Mowing

Door Hanger- Heron Yards LLC. I would like the Heron Logo on a white background with three shades of pink incorporated into the flyer. Our phone number is 555-203-7486. And our website is heronyardcrew.example. I would like for the door hanger to mirror the Oakmere Door Hanger, using the Heron logo & information.

List of Services to include:
Pest Control
Termite Inspection
Lawn Maintenance
Debris Clean-up
Trash Removal
Home Inspection
Handy-man Services

Target Market(s)

Residential Lawns

Industry/Entity Type

Lawn Care

Font styles to use
Sans Serif

Colors
e34197
e667a6
eea4c8
f9d9e8

Requirements
Must have
• Phone Number
• Must be a Door Hanger
• Website
• 2 Sided
Nice to have
• 3 Shades of Pink with white background
Should not have
• It must be a door hanger. KEEP IN MIND THERE WILL BE A PUNCH HOLE AT TOP.......

```html
<!DOCTYPE html>
<html lang="en">
<head>
<meta charset="utf-8">
<title>Heron Yards LLC – Door Hanger</title>
<link rel="stylesheet" href="https://fonts.googleapis.com/css2?family=Montserrat:wght@400;500;700&family=Oswald:wght@400;600;700&display=swap">
<style>
  :root {
    --pink-deep: #e34197;
    --pink-mid: #e667a6;
    --pink-soft: #eea4c8;
    --pink-blush: #f9d9e8;
    --white: #ffffff;
    --ink: #3a3a3a;
    --grass: #45b649;
    --backdrop: #2b2c2f;
  }
  * { box-sizing: border-box; margin: 0; padding: 0; }
  html, body { width: 1200px; height: 900px; overflow: hidden; }
  body {
    background: var(--backdrop);
    font-family: "Montserrat", sans-serif;
    position: relative;
  }
  .hanger {
    position: absolute;
    top: 50px;
    width: 330px;
    height: 800px;
    overflow: hidden;
    border-radius: 4px;
  }
  .hanger--front { left: 230px; background: var(--white); }
  .hanger--back {
    left: 640px;
    background: linear-gradient(160deg, var(--pink-mid) 0%, var(--pink-deep) 55%, var(--pink-deep) 100%);
  }
  .hanger__art { position: absolute; inset: 0; width: 100%; height: 100%; }
  .punch-hole {
    position: absolute;
    top: 38px; left: 50%;
    width: 84px; height: 84px;
    margin-left: -42px;
    border-radius: 50%;
    background: var(--backdrop);
    z-index: 3;
  }
  .brand {
    position: absolute;
    top: 150px; left: 0; right: 0;
    display: flex; align-items: center; justify-content: center; gap: 10px;
    z-index: 2;
  }
  .brand__dot { width: 18px; height: 18px; border-radius: 50%; background: var(--pink-deep); }
  .brand__name {
    font-family: "Oswald", sans-serif;
    font-weight: 600;
    font-size: 40px;
    letter-spacing: 1px;
    text-transform: uppercase;
    color: var(--ink);
    white-space: nowrap;
  }
  .hanger--back .brand__dot { background: var(--white); }
  .hanger--back .brand__name { color: var(--white); }

  .offer { position: absolute; top: 270px; left: 30px; right: 30px; z-index: 2; }
  .offer__title {
    font-weight: 700; font-size: 24px; letter-spacing: 1.5px; color: var(--ink);
    margin-bottom: 12px;
  }
  .offer__text { font-size: 15px; line-height: 1.35; color: var(--ink); font-weight: 500; }

  .price-box {
    position: absolute; top: 430px; left: 30px; right: 30px; height: 150px;
    background: var(--white); border-radius: 14px; z-index: 2;
  }
  .price-box__currency {
    position: absolute; left: 14px; bottom: 12px;
    font-size: 30px; color: var(--pink-deep); font-weight: 500;
  }
  .price-box__unit {
    position: absolute; right: 14px; top: 10px;
    font-size: 11px; color: var(--pink-deep);
  }

  .cta { position: absolute; left: 24px; right: 24px; z-index: 2; color: var(--white); }
  .cta__lead { font-size: 16px; font-weight: 500; white-space: nowrap; }
  .cta__phone {
    font-family: "Oswald", sans-serif; font-weight: 700;
    font-size: 42px; line-height: 1.1; letter-spacing: 0.5px;
    white-space: nowrap;
  }
  .cta__web { font-size: 13px; font-weight: 500; margin-top: 2px; white-space: nowrap; }
  .hanger--front .cta { top: 598px; }
  .hanger--back .cta { top: 598px; }

  .grass { position: absolute; left: 0; right: 0; bottom: 0; height: 80px; z-index: 1; }
  .hanger--front .grass { background: var(--grass); }
  .hanger--back .grass { background: var(--white); }

  .services { position: absolute; top: 270px; left: 40px; right: 30px; color: var(--white); z-index: 2; }
  .services__title { font-size: 22px; font-weight: 700; margin-bottom: 14px; }
  .services__list { list-style: none; font-size: 17px; line-height: 1.5; }
  .services__list li::before { content: "•"; margin-right: 8px; }
</style>
</head>
<body>

  <section class="hanger hanger--front" aria-label="Door hanger front">
    <svg class="hanger__art" viewBox="0 0 330 800" preserveAspectRatio="none" aria-hidden="true">
      <path d="M330 120 C 280 220, 200 300, 120 340 L 330 340 Z" fill="var(--pink-blush)"/>
      <path d="M330 200 C 270 320, 170 420, 60 470 L 330 470 Z" fill="var(--pink-soft)"/>
      <path d="M330 280 C 260 410, 140 480, 0 520 L 0 800 L 330 800 Z" fill="var(--pink-mid)"/>
      <path d="M330 380 C 250 480, 130 540, 0 570 L 0 800 L 330 800 Z" fill="var(--pink-deep)"/>
    </svg>
    <div class="punch-hole"></div>
    <div class="brand"><span class="brand__dot"></span><span class="brand__name">Heron Yards</span></div>
    <div class="offer">
      <h2 class="offer__title">LAWN MOWING</h2>
      <p class="offer__text">We keep your lawn green, healthy and free of weeds. Aeration, Fertilization and regular landscaping services.</p>
    </div>
    <div class="price-box">
      <span class="price-box__unit">per service</span>
      <span class="price-box__currency">$</span>
    </div>
    <div class="cta">
      <p class="cta__lead">call to schedule service today</p>
      <p class="cta__phone">555-203-7486</p>
      <p class="cta__web">heronyardcrew.example</p>
    </div>
    <div class="grass" role="img" aria-label="Green grass silhouette along the bottom edge"></div>
  </section>

  <section class="hanger hanger--back" aria-label="Door hanger back">
    <div class="punch-hole"></div>
    <div class="brand"><span class="brand__dot"></span><span class="brand__name">Heron Yards</span></div>
    <div class="services">
      <h2 class="services__title">Additional services:</h2>
      <ul class="services__list">
        <li>Pest Control</li>
        <li>Termite Inspection</li>
        <li>Lawn Maintenance</li>
        <li>Debris Clean-up</li>
        <li>Trash Removal</li>
        <li>Home Inspection</li>
        <li>Handy-man Services</li>
      </ul>
    </div>
    <div class="cta">
      <p class="cta__lead">call today for a free estimate</p>
      <p class="cta__phone">555-203-7486</p>
      <p class="cta__web">heronyardcrew.example</p>
    </div>
    <div class="grass" role="img" aria-label="White grass silhouette along the bottom edge"></div>
  </section>

</body>
</html>
```